Quarry IT Services Business Card

Quarry IT Services are a Perth based IT Services company. We would like to incorporate our company logo (attached) and stick with the blue that is in that design. I would like a clean look design that isn't too busy, yet creates a lasting image that is instantly recognisable in the recipients mind.

Target Market(s)

The target audience is small/medium business owners.

Industry/Entity Type

Business

Font styles to use
Serif
Sans Serif

Colors

Designer to choose colors to be used in the design.

Requirements
Must have
• The design should include:
Business name: Quarry IT Services
Directors Name: Darren Mowley
Phone Number: 0462 830 514
Email: support@quarryit.com.au
Website: www.quarryit.com.au

```html
<!DOCTYPE html>
<html lang="en">
<head>
<meta charset="utf-8">
<title>Quarry IT Services – Business Card</title>
<link rel="stylesheet" href="https://fonts.googleapis.com/css2?family=Arimo:wght@400;700&family=Play:wght@700&display=swap">
<style>
  :root {
    --backdrop: #dde7f7;
    --backdrop-edge: #c9d8f1;
    --card-dark: #3a3a3a;
    --card-light: #ffffff;
    --brand-blue: #2a5caa;
    --ink: #333333;
    --on-dark: #f2f2f2;
  }
  * { margin: 0; padding: 0; box-sizing: border-box; }
  html, body {
    width: 1200px; height: 965px; overflow: hidden;
    background: radial-gradient(ellipse at center, #e6eefb 0%, var(--backdrop) 55%, var(--backdrop-edge) 100%);
    font-family: "Arimo", Arial, sans-serif;
  }
  .card {
    position: absolute; left: 285px; width: 630px; height: 360px;
    box-shadow: 0 4px 10px rgba(40, 60, 100, 0.25);
    overflow: hidden;
  }
  .card-front { top: 80px; background: var(--card-dark); }
  .card-back { top: 525px; background: var(--card-light); }

  .wordmark {
    position: absolute; display: flex; align-items: center; gap: 10px;
    color: var(--brand-blue); font-weight: 700;
  }
  .wordmark .mark-square { width: 22px; height: 22px; background: currentColor; flex: none; }
  .wordmark .name { line-height: 1; }
  .wordmark .name-main { display: block; font-size: 36px; letter-spacing: 1px; }
  .wordmark .name-sub { display: block; font-size: 10px; letter-spacing: 7px; margin-top: 4px; }
  .card-front .wordmark { left: 355px; top: 250px; color: var(--on-dark); }
  .card-front .wordmark .mark-square { background: var(--brand-blue); }
  .card-back .wordmark { left: 395px; top: 100px; }

  .front-web {
    position: absolute; right: 50px; top: 310px;
    color: var(--on-dark); font-size: 19px;
  }

  .id-tab {
    position: absolute; left: 0; top: 234px; width: 19px; height: 38px;
    background: var(--brand-blue); border-radius: 0 8px 8px 0;
  }
  .person { position: absolute; left: 43px; top: 235px; }
  .person-name {
    font-family: "Play", "Arimo", sans-serif; font-weight: 700;
    color: var(--brand-blue); font-size: 19px; line-height: 1;
  }
  .person-title { color: var(--ink); font-size: 14.5px; margin-top: 3px; }

  .contact-list {
    position: absolute; left: 348px; top: 235px; list-style: none;
    color: var(--ink); font-size: 15px; line-height: 18.5px;
  }
  .contact-list li { display: flex; align-items: center; gap: 7px; }
  .contact-list svg { width: 17px; height: 14px; flex: none; fill: var(--brand-blue); }

  .footer-bands { position: absolute; left: 0; bottom: 0; width: 630px; height: 40px; }
</style>
</head>
<body>
  <section class="card card-front" aria-label="Card front">
    <div class="wordmark">
      <span class="mark-square"></span>
      <span class="name"><span class="name-main">QUARRY</span><span class="name-sub">IT SERVICES</span></span>
    </div>
    <p class="front-web">www.quarryit.com.au</p>
  </section>

  <section class="card card-back" aria-label="Card back">
    <div class="wordmark">
      <span class="mark-square"></span>
      <span class="name"><span class="name-main">QUARRY</span><span class="name-sub">IT SERVICES</span></span>
    </div>

    <div class="id-tab"></div>
    <div class="person">
      <p class="person-name">Darren Mowley</p>
      <p class="person-title">Managing Director</p>
    </div>

    <ul class="contact-list">
      <li>
        <svg viewBox="0 0 17 14" aria-hidden="true"><path d="M1 5 Q8.5 -1 16 5 L13 6.5 L12 4.5 Q8.5 3 5 4.5 L4 6.5 Z"/><rect x="4" y="7" width="9" height="6" rx="1"/></svg>
        <span>0462 830 514</span>
      </li>
      <li>
        <svg viewBox="0 0 17 14" aria-hidden="true"><path d="M1 2 H16 V13 H1 Z M2.5 3.5 V11.5 H14.5 V3.5 L8.5 8 Z" fill-rule="evenodd"/></svg>
        <span>support@quarryit.com.au</span>
      </li>
      <li>
        <svg viewBox="0 0 17 17" aria-hidden="true" style="height:16px"><circle cx="8.5" cy="8.5" r="7.5" fill="none" stroke="#2a5caa" stroke-width="1.5"/><ellipse cx="8.5" cy="8.5" rx="3.2" ry="7.5" fill="none" stroke="#2a5caa" stroke-width="1.3"/><path d="M1 8.5 H16 M2.5 4.5 H14.5 M2.5 12.5 H14.5" stroke="#2a5caa" stroke-width="1.2"/></svg>
        <span>www.quarryit.com.au</span>
      </li>
    </ul>

    <svg class="footer-bands" viewBox="0 0 630 40" aria-hidden="true">
      <polygon points="0,4 190,4 209,22 630,22 630,40 0,40" fill="#2a5caa"/>
      <polygon points="198,10 630,10 630,20 208,20" fill="#3a3a3a"/>
    </svg>
  </section>
</body>
</html>
```